HOLLOWPINE SPIRITS WEBSITE

HOLLOWPINE SPIRITS WHOLESALES ALCOHOL (WHISKY VODKA AND HELPS CREATES BOTTLING/BRANDING FOR PEOPLE WANTING LAUNCH THERE OWN BRANDS OF ALCOHOL

Colors

Designer to choose colors to be used in the design.

```html
<!DOCTYPE html>
<html lang="en">
<head>
<meta charset="utf-8">
<title>Hollowpine Spirits</title>
<link href="https://fonts.googleapis.com/css2?family=Montserrat:wght@400;500;600&family=Caveat:wght@500&display=swap" rel="stylesheet">
<style>
:root{
  --page:#ffffff;
  --ink-dark:#2d2a26;
  --gold:#8a7a45;
  --gold-line:#c9bf9f;
  --text:#2b2b2b;
  --script:#6f6438;
  --white:#ffffff;
}
*{margin:0;padding:0;box-sizing:border-box}
html,body{width:1200px;height:2190px;overflow:hidden;background:var(--page);font-family:'Montserrat',sans-serif}
.canvas{position:relative;width:1200px;height:2190px}
.site{position:absolute;left:136px;top:258px;width:925px;height:1678px;box-shadow:0 0 22px rgba(0,0,0,.28);overflow:hidden}
.nav{position:absolute;left:0;top:0;width:925px;height:66px;background:var(--ink-dark);display:flex;align-items:center;justify-content:space-between;padding:0 48px 0 52px}
.brand{display:flex;align-items:center;gap:10px;color:var(--white);font-weight:500;font-size:16px;letter-spacing:1px}
.brand-mark{width:14px;height:14px;background:var(--gold)}
.menu{display:flex;gap:34px;list-style:none}
.menu li{color:var(--white);font-size:11.5px;letter-spacing:.3px}
.hero{position:absolute;top:66px;left:0;width:925px;height:361px;display:flex}
.hero-photo{width:448px;height:361px;background:radial-gradient(circle at 65% 45%,#c58a3a 0,#7a3f1c 35%,#3d2415 75%,#2a1a10 100%)}
.hero-product{position:relative;flex:1;height:361px;background:radial-gradient(circle at 45% 50%,#ffffff 0,#ececec 60%,#d4d4d4 100%)}
.product-shot{position:absolute;left:170px;top:40px;width:125px;height:290px;background:radial-gradient(ellipse 50% 50% at 50% 52%,rgba(60,45,25,.85) 0,rgba(120,80,30,.45) 55%,rgba(255,255,255,0) 100%)}
.tagline{position:absolute;left:22px;top:155px;width:140px;font-family:'Caveat',cursive;font-weight:500;font-size:27px;line-height:30px;color:var(--script);text-align:center}
.tagline-arrow{position:absolute;left:24px;top:250px;width:130px;height:34px}
.welcome{position:absolute;top:427px;left:0;width:925px;height:621px;background:radial-gradient(ellipse at 50% 55%,#ffffff 0,#f2f2f2 55%,#e6e6e6 100%);text-align:center}
.welcome h1{position:absolute;top:72px;width:100%;font-weight:600;font-size:47px;line-height:56px;color:var(--gold)}
.welcome .lead{position:absolute;top:140px;width:100%;font-weight:500;font-size:19.5px;line-height:24px;color:var(--text)}
.rule{position:absolute;top:202px;left:328px;width:285px;height:1px;background:var(--gold-line)}
.intro{position:absolute;top:226px;left:152px;width:620px;font-size:13px;line-height:35px;color:var(--text)}
.step{position:absolute;top:366px;width:166px;height:166px;border-radius:50%;box-shadow:4px 6px 12px rgba(0,0,0,.3)}
.step-one{left:110px;background:radial-gradient(circle at 55% 40%,#d8d6c8 0,#6f6a55 45%,#1e1e1e 100%)}
.step-two{left:382px;background:radial-gradient(circle at 50% 50%,#b9a7c9 0,#8a6f9a 45%,#4a3a55 100%)}
.step-three{left:654px;background:radial-gradient(circle at 50% 50%,#c9c9c9 0,#6d6d6d 50%,#2a2a2a 100%)}
.flow-arrow{position:absolute;top:420px;width:90px;height:50px}
.about{position:absolute;top:1048px;left:0;width:925px;height:630px;background:linear-gradient(#4a4640 0,#3a3631 45%,var(--ink-dark) 70%,var(--ink-dark) 100%);text-align:center}
.about h2{position:absolute;top:282px;width:100%;font-weight:600;font-size:47px;line-height:56px;color:var(--gold)}
.about-copy{position:absolute;top:350px;left:210px;width:505px;font-size:13px;line-height:27px;color:var(--white)}
.about-copy p+p{margin-top:17px}
</style>
</head>
<body>
<div class="canvas">
  <div class="site">
    <header class="nav">
      <div class="brand"><span class="brand-mark"></span>HOLLOWPINE SPIRITS</div>
      <ul class="menu"><li>HOME</li><li>ABOUT</li><li>WHOLESALE</li><li>SERVICES</li><li>CONTACT</li></ul>
    </header>
    <section class="hero">
      <div class="hero-photo" role="img" aria-label="Glass of whisky on ice resting on an oak barrel"></div>
      <div class="hero-product">
        <p class="tagline">Your next drink idea into a reality</p>
        <svg class="tagline-arrow" viewBox="0 0 130 34"><path d="M2 26 C40 34 90 30 124 14" fill="none" stroke="#6f6438" stroke-width="2"/><path d="M112 8 L125 13 L116 24" fill="none" stroke="#6f6438" stroke-width="2"/></svg>
        <div class="product-shot" role="img" aria-label="Whisky bottle with a blank label reading your brand"></div>
      </div>
    </section>
    <section class="welcome">
      <h1>Welcome to Hollowpine</h1>
      <p class="lead">Turn your next drink idea into a reality and share your product with the world.</p>
      <div class="rule"></div>
      <p class="intro">Hollowpine can bring your vision to life with our inhouse teams. We are here to help you through the entire process of creating unique spirit to compliment your brand. From formulating the recipe to production and even to helping you market your newest drink;</p>
      <div class="step step-one" role="img" aria-label="Gin cocktail with lemon and lime"></div>
      <svg class="flow-arrow" style="left:285px" viewBox="0 0 90 50"><path d="M4 40 C20 18 32 22 34 34 C36 44 52 30 80 16" fill="none" stroke="#bdbdbd" stroke-width="1.6"/><path d="M70 14 L82 15 L76 25" fill="none" stroke="#bdbdbd" stroke-width="1.6"/></svg>
      <div class="step step-two" role="img" aria-label="Worker on a bottling production line"></div>
      <svg class="flow-arrow" style="left:556px" viewBox="0 0 90 50"><path d="M4 40 C20 18 32 22 34 34 C36 44 52 30 80 16" fill="none" stroke="#bdbdbd" stroke-width="1.6"/><path d="M70 14 L82 15 L76 25" fill="none" stroke="#bdbdbd" stroke-width="1.6"/></svg>
      <div class="step step-three" role="img" aria-label="Stainless steel distilling tanks"></div>
    </section>
    <section class="about" role="img" aria-label="Long warehouse aisle lined with stacked oak barrels">
      <h2>ABOUT</h2>
      <div class="about-copy">
        <p>Hollowpine Spirits, located in the Netherlands, has been mixing creating 5-star-rated gin, cocktails and making recipes since 2017. Now we want to use our distilling expertise to help you launch your very own brand of liquor.</p>
        <p>Through our vast network we have exclusive access some of the best Whiskies, Vodka, Rum, Gins and Wines in the world.</p>
        <p>We work directly with you to develop the perfect recipe and produce your drink</p>
      </div>
    </section>
  </div>
</div>
</body>
</html>
```